Website for a web design agency

We are a website and marketing agency. We do website design, development, and well as Brindle and Quorvia advertising and analytics. We ourselves need a new website for our own brand. We are working on some designs in-house with our own designers, but we also wanted to see what outside designers would come up with.
We are starting off with the homepage, and here is the breakdown of the sections:
https://files.brindlework.example/sheet/d/7kqTr2VnPLwXeHsaMcY4oBfJzuGNtKdWiEh3Rx9pLmQb/view?mode=share
This doc also has many links to sites we have done, which you can take screenshots of for the portfolio section.
In terms of the "look" I am going for, I want to look high-end and very beautiful designs. I found this website that I like a lot that you can use some of the elements of, just as a starting point:
http://velmarkstudio.example/layouts/pixelbarn/html/ostrevo/index.html and here is another design option they have http://velmarkstudio.example/layouts/pixelbarn/html/ostrevo/index-4.html
I'm also uploading my logo. The logo matches the gold and black look from these websites, but I would be open to switching to another color scheme if needed.
This is the link to my very old website, which you can use for some of the dummy text, and a pic of myself. I will be taking more pics of myself:
https://theplumtreeandwillowgroup.example/
We need a homepage and a portfolio page right now, but if you are the winner, we will be hiring you to make additional pages.
Updates
More designs continue to come in even today, and I want to make sure no other designers are still submitting designs.
Target Market(s)
medium and large businesses owners, and non-profits
Number of Pages Required
1 page

```html
<!DOCTYPE html>
<html lang="en">
<head>
<meta charset="utf-8">
<title>Varden Strategies — Home</title>
<link href="https://fonts.googleapis.com/css2?family=Playfair+Display:wght@700;800&family=Poppins:ital,wght@0,400;0,500;0,600;1,400&display=swap" rel="stylesheet">
<style>
:root{
  --bg:#1c1b21;
  --panel:#26252b;
  --card:#3a3940;
  --gold:#e8b540;
  --gold-deep:#d9a52f;
  --text:#ffffff;
  --muted:#d6d4da;
  --line:#7b7985;
}
*{box-sizing:border-box;margin:0;padding:0}
html,body{width:1200px;height:3891px;overflow:hidden;background:var(--bg)}
body{font-family:"Poppins",sans-serif;color:var(--text);position:relative}
.page{position:relative;width:1200px;height:3891px;overflow:hidden;background:var(--bg)}
.abs{position:absolute}
.band{position:absolute;left:0;width:1200px}
.band--panel{background:var(--panel)}
.serif{font-family:"Playfair Display",serif;font-weight:700}

/* header */
.logo{left:116px;top:16px;width:120px;color:var(--gold);text-align:center}
.logo__name{font-family:"Poppins",sans-serif;font-weight:600;font-size:24px;line-height:24px;letter-spacing:1px}
.logo__sub{font-size:10px;letter-spacing:4px;line-height:14px}
.nav{top:28px;font-size:15px}
.nav a{position:absolute;color:var(--text);text-decoration:none;white-space:nowrap}
.nav a.is-active{color:var(--gold)}
.nav a.is-active::after{content:"";position:absolute;left:50%;transform:translateX(-50%);top:28px;width:22px;height:2px;background:var(--gold)}

/* hero */
.hero-panel{left:283px;top:0;width:917px;height:517px;background:var(--panel)}
.hero__title{left:104px;top:182px;font-size:37px;letter-spacing:.3px}
.hero__lead{left:104px;top:243px;width:430px;font-size:19px;line-height:27px}
.btn{position:absolute;background:var(--gold);color:var(--text);font-size:14px;display:flex;align-items:center;justify-content:center;box-shadow:0 8px 18px rgba(232,181,64,.25)}
.hero__btn{left:104px;top:334px;width:198px;height:41px;text-transform:uppercase}
.photo{position:absolute}
.hero__photo{left:713px;top:98px;width:381px;height:493px;background:linear-gradient(160deg,#e9e9ea 0%,#c9cbcf 45%,#8f9096 100%)}
.play{left:870px;top:316px;width:66px;height:66px;border-radius:50%;background:rgba(70,70,78,.75)}

/* sections */
.section-title{left:0;width:1200px;text-align:center;font-size:23px}
.section-rule{left:580px;width:40px;height:2px;background:var(--gold)}
.section-sub{left:0;width:1200px;text-align:center;font-size:15px}
.section-sub b{font-weight:600}

/* services */
.service{position:absolute;width:301px;height:141px;background:var(--card);border-radius:3px}
.service--active{background:var(--gold)}
.service__icon{position:absolute;left:20px;top:34px;width:74px;height:74px}
.service__title{position:absolute;left:110px;top:34px;width:170px;font-size:17px;line-height:24px;padding-bottom:8px;border-bottom:1px solid var(--line)}
.service--active .service__title{border-bottom-color:rgba(255,255,255,.7)}
.service__text{position:absolute;left:110px;width:175px;font-size:12px;line-height:17px;color:var(--muted)}
.service--active .service__text{color:#fff5dc}

/* portfolio */
.frame{position:absolute;border:4px solid var(--gold)}
.work{position:absolute;width:301px;height:331px;background:var(--card)}
.work__shot{position:absolute;left:6px;top:4px;width:289px;height:154px}
.work__title{position:absolute;left:12px;top:176px;font-size:17px;font-weight:500;padding-top:10px;border-top:1px solid var(--line);width:277px}
.work__text{position:absolute;left:12px;top:216px;width:275px;font-size:12px;line-height:17px;color:var(--muted)}
.work__btn{left:12px;top:291px;width:92px;height:23px;font-size:11px;box-shadow:none}
.pager{position:absolute;width:10px;height:10px;border-radius:50%;background:#fff}
.pager.is-on{background:var(--gold)}

/* testimonials */
.portrait{position:absolute;background:var(--gold)}
.portrait__fill{position:absolute;inset:0;background:linear-gradient(180deg,#e8b540 0%,#d3a448 45%,#8a6a48 100%)}
.sq{position:absolute;border:4px solid var(--gold-deep)}
.quote{position:absolute;font-size:18px;line-height:26px;width:440px}
.quote__mark{position:absolute;color:var(--gold);font-family:"Playfair Display",serif;font-size:28px;line-height:1}
.person__name{position:absolute;color:var(--gold);font-size:15px;font-weight:500}
.person__role{position:absolute;font-size:15px;font-style:italic}
.arrow{position:absolute;width:41px;height:41px;border:2px solid var(--gold);display:flex;align-items:center;justify-content:center}
.arrow--fill{background:var(--gold)}

/* team */
.member{position:absolute;width:194px;height:241px;border:3px solid var(--gold)}
.member__photo{position:absolute;left:4px;top:4px;right:4px;bottom:4px}
.member__name{position:absolute;top:2980px;color:var(--gold);font-size:15px;font-weight:500}
.member__role{position:absolute;top:3003px;font-size:15px;font-style:italic}
.team__btn{left:500px;top:3090px;width:198px;height:41px;font-size:15px}

/* contact */
.pitch{left:104px;top:3428px;font-size:26px;line-height:38px;font-weight:500}
.pitch em{font-style:normal;color:var(--gold)}
.contact-label{font-size:15px}
.contact-line{display:flex;align-items:center;gap:14px;font-size:17px;font-weight:500}
.field{position:absolute;left:555px;width:539px;height:42px;border:1px solid #9a98a2;font-size:14px;padding:10px 18px;color:#e6e4ea}
.send{left:555px;top:3723px;width:539px;height:43px;font-size:16px;font-weight:600;letter-spacing:1px;gap:8px;box-shadow:none}

/* footer */
.footer{left:0;top:3843px;width:1200px;height:48px;background:var(--gold)}
.footer__text{position:absolute;left:104px;top:14px;font-size:16px;font-weight:600;letter-spacing:.3px}
.social{position:absolute;top:15px;width:19px;height:19px;background:#fff;border-radius:4px;opacity:.9}
</style>
</head>
<body>
<div class="page">
  <svg width="0" height="0" style="position:absolute">
    <defs>
      <pattern id="dots" width="28.6" height="28.6" patternUnits="userSpaceOnUse">
        <circle cx="3" cy="3" r="3" fill="#e8b540"/>
      </pattern>
      <pattern id="dots-sm" width="14" height="14" patternUnits="userSpaceOnUse">
        <circle cx="2" cy="2" r="1.8" fill="#e8b540"/>
      </pattern>
    </defs>
  </svg>

  <!-- header & hero -->
  <div class="hero-panel"></div>
  <div class="abs logo"><div class="logo__name">VARDEN</div><div class="logo__sub">STRATEGIES</div></div>
  <nav class="abs nav" style="left:0;top:28px;width:1200px">
    <a class="is-active" style="left:571px">Home</a>
    <a style="left:662px">Services</a>
    <a style="left:770px">Portofolio</a>
    <a style="left:887px">Testimonials</a>
    <a style="left:1027px">Contacts</a>
  </nav>

  <svg class="abs" style="left:966px;top:74px" width="210" height="180"><rect x="0" y="0" width="210" height="7" fill="url(#dots)"/><rect x="142" y="28" width="68" height="152" fill="url(#dots)"/></svg>
  <svg class="abs" style="left:662px;top:469px" width="210" height="180"><rect x="0" y="0" width="35" height="130" fill="url(#dots)"/><rect x="0" y="143" width="210" height="35" fill="url(#dots)"/></svg>

  <h1 class="abs serif hero__title">We Build Value.</h1>
  <p class="abs hero__lead">Enterprise Level Website Development and Online Marketing</p>
  <div class="btn hero__btn">See how we do it</div>
  <div class="photo hero__photo" role="img" aria-label="Photo of a designer sketching ideas on a wall board"></div>
  <div class="abs play"><svg width="66" height="66"><path d="M27 21 L46 33 L27 45 Z" fill="#fff"/></svg></div>

  <!-- what we do -->
  <h2 class="abs serif section-title" style="top:702px">What we do</h2>
  <div class="abs section-rule" style="top:740px"></div>
  <p class="abs section-sub" style="top:768px">These are things we <b>CRUSH.</b></p>

  <div class="service service--active" style="left:104px;top:840px">
    <svg class="service__icon" viewBox="0 0 74 74" fill="none" stroke="#fff" stroke-width="2"><rect x="6" y="10" width="62" height="42" rx="3"/><line x1="6" y1="18" x2="68" y2="18"/><rect x="14" y="25" width="46" height="18"/><line x1="30" y1="52" x2="26" y2="64"/><line x1="44" y1="52" x2="48" y2="64"/><line x1="20" y1="64" x2="54" y2="64"/></svg>
    <div class="service__title">Websites</div>
    <div class="service__text" style="top:74px">Lorem ipsum dolor sit amet, consectetur adipiscing elit.</div>
  </div>
  <div class="service" style="left:450px;top:840px">
    <svg class="service__icon" viewBox="0 0 74 74" fill="none" stroke="#fff" stroke-width="2"><rect x="4" y="6" width="66" height="60" rx="3"/><line x1="4" y1="16" x2="70" y2="16"/><rect x="12" y="24" width="26" height="20"/><path d="M12 42 L22 32 L30 40 L38 34"/><line x1="44" y1="26" x2="62" y2="26"/><line x1="44" y1="34" x2="62" y2="34"/><line x1="44" y1="42" x2="62" y2="42"/><circle cx="16" cy="56" r="4"/><circle cx="29" cy="56" r="4"/><circle cx="42" cy="56" r="4"/><circle cx="55" cy="56" r="4"/></svg>
    <div class="service__title">Landing Pages</div>
    <div class="service__text" style="top:74px">Lorem ipsum dolor sit amet, consectetur adipiscing elit.</div>
  </div>
  <div class="service" style="left:795px;top:840px">
    <svg class="service__icon" viewBox="0 0 74 74" fill="none" stroke="#fff" stroke-width="2"><rect x="4" y="6" width="66" height="60" rx="3"/><line x1="4" y1="16" x2="70" y2="16"/><circle cx="37" cy="32" r="9"/><path d="M37 26 V38 M34 29 H40 M34 35 H40"/><rect x="10" y="48" width="54" height="12"/></svg>
    <div class="service__title">Donation Pages</div>
    <div class="service__text" style="top:74px">Lorem ipsum dolor sit amet, consectetur adipiscing elit.</div>
  </div>
  <div class="service" style="left:104px;top:1027px">
    <svg class="service__icon" viewBox="0 0 74 74" fill="none" stroke="#fff" stroke-width="2"><rect x="8" y="10" width="58" height="42" rx="4"/><rect x="14" y="16" width="46" height="30"/><line x1="4" y1="58" x2="70" y2="58"/><circle cx="35" cy="31" r="9"/><path d="M35 25 V37"/><path d="M44 36 L52 44"/></svg>
    <div class="service__title">PPC and Funnels</div>
    <div class="service__text" style="top:74px">Lorem ipsum dolor sit amet, consectetur adipiscing elit.</div>
  </div>
  <div class="service" style="left:450px;top:1027px">
    <svg class="service__icon" viewBox="0 0 74 74" fill="none" stroke="#fff" stroke-width="2"><rect x="8" y="28" width="58" height="38" rx="3"/><path d="M8 28 L62 12 L64 20 L10 36"/><line x1="8" y1="36" x2="66" y2="36"/><path d="M32 42 L46 50 L32 58 Z"/></svg>
    <div class="service__title">Video Marketing</div>
    <div class="service__text" style="top:74px">Lorem ipsum dolor sit amet, consectetur adipiscing elit.</div>
  </div>
  <div class="service" style="left:795px;top:1027px">
    <svg class="service__icon" viewBox="0 0 74 74" fill="none" stroke="#fff" stroke-width="2"><rect x="4" y="6" width="66" height="62" rx="3"/><line x1="4" y1="16" x2="70" y2="16"/><path d="M12 44 L26 30 L38 38 L58 24"/><rect x="14" y="50" width="8" height="14"/><rect x="30" y="46" width="8" height="18"/><rect x="46" y="42" width="8" height="22"/></svg>
    <div class="service__title" style="top:22px">Analytic &amp;<br>Optimization</div>
    <div class="service__text" style="top:84px">Lorem ipsum dolor sit amet, consectetur adipiscing elit.</div>
  </div>

  <!-- portfolio -->
  <div class="band band--panel" style="top:1204px;height:558px"></div>
  <h2 class="abs serif section-title" style="top:1226px">Portofolio</h2>
  <div class="abs section-rule" style="top:1264px"></div>
  <p class="abs section-sub" style="top:1292px">Here some of our recent projects.</p>

  <div class="frame" style="left:77px;top:1333px;width:263px;height:284px;border-right:none;border-bottom:none"></div>
  <div class="frame" style="left:860px;top:1435px;width:261px;height:285px;border-left:none;border-top:none"></div>

  <div class="work" style="left:104px;top:1361px">
    <div class="work__shot" role="img" aria-label="Screenshot of the Loftwell website homepage" style="background:linear-gradient(120deg,#3a2f27 0%,#8a7360 55%,#d7cbbd 100%)"></div>
    <div class="work__title">Loftwell Website</div>
    <div class="work__text">Lorem ipsum dolor sit amet, consectetur adipiscing elit, sed do eiusmod tempor incididunt ut labore et dolore magna aliqua.</div>
    <div class="btn work__btn">Read more</div>
  </div>
  <div class="work" style="left:450px;top:1361px">
    <div class="work__shot" role="img" aria-label="Screenshot of the Kelvantro Production website homepage" style="background:linear-gradient(90deg,#0f2a6b 0%,#1f4fa8 60%,#4a78c9 100%)"></div>
    <div class="work__title">Kelvantro Production</div>
    <div class="work__text">Lorem ipsum dolor sit amet, consectetur adipiscing elit, sed do eiusmod tempor incididunt ut labore et dolore magna aliqua.</div>
    <div class="btn work__btn">Read more</div>
  </div>
  <div class="work" style="left:795px;top:1361px">
    <div class="work__shot" role="img" aria-label="Screenshot of the Nuvetric portfolio homepage" style="background:linear-gradient(180deg,#f4f4f4 0%,#f4f4f4 8%,#101010 9%,#101010 88%,#f2f2f2 89%)"></div>
    <div class="work__title">Nuvetric Portofolio</div>
    <div class="work__text">Lorem ipsum dolor sit amet, consectetur adipiscing elit, sed do eiusmod tempor incididunt ut labore et dolore magna aliqua.</div>
    <div class="btn work__btn">Read more</div>
  </div>

  <div class="pager is-on" style="left:554px;top:1727px"></div>
  <div class="pager" style="left:581px;top:1727px"></div>
  <div class="pager" style="left:607px;top:1727px"></div>
  <div class="pager" style="left:634px;top:1727px"></div>

  <!-- testimonials -->
  <h2 class="abs serif section-title" style="top:1820px">Testimonials &nbsp;and Case study</h2>
  <div class="abs section-rule" style="top:1858px"></div>
  <p class="abs section-sub" style="top:1885px">Here some of testimonial from our clients.</p>

  <svg class="abs" style="left:81px;top:1956px" width="104" height="90"><rect width="104" height="8" fill="url(#dots-sm)"/><rect y="14" width="104" height="8" fill="url(#dots-sm)"/><rect y="28" width="34" height="62" fill="url(#dots-sm)"/></svg>
  <div class="portrait" style="left:122px;top:1998px;width:206px;height:205px"><div class="portrait__fill" role="img" aria-label="Portrait photo of client Alexander"></div></div>
  <div class="sq" style="left:292px;top:2162px;width:57px;height:59px"></div>

  <span class="quote__mark" style="left:375px;top:2003px">“</span>
  <p class="quote" style="left:397px;top:2004px">Lorem ipsum dolor sit amet, consectetur adipiscing elit, sed do eiusmod tempor incididunt ut labore et dolore magna aliqua. <span style="color:var(--gold);font-family:'Playfair Display',serif">”</span></p>
  <div class="person__name" style="left:397px;top:2101px">Alexander</div>
  <div class="person__role" style="left:397px;top:2124px">CEO, Loftwell</div>

  <div class="arrow" style="left:1000px;top:1998px"><svg width="20" height="14" fill="none" stroke="#fff" stroke-width="2"><path d="M19 7 H2 M8 1 L2 7 L8 13"/></svg></div>
  <div class="arrow arrow--fill" style="left:1053px;top:1998px"><svg width="20" height="14" fill="none" stroke="#1c1b21" stroke-width="2"><path d="M1 7 H18 M12 1 L18 7 L12 13"/></svg></div>

  <span class="quote__mark" style="left:375px;top:2287px">“</span>
  <p class="quote" style="left:397px;top:2288px">Lorem ipsum dolor sit amet, consectetur adipiscing elit, sed do eiusmod tempor incididunt ut labore et dolore magna aliqua. <span style="color:var(--gold);font-family:'Playfair Display',serif">”</span></p>
  <div class="person__name" style="left:747px;top:2385px">Alexander</div>
  <div class="person__role" style="left:724px;top:2408px">CEO, Loftwell</div>

  <div class="portrait" style="left:873px;top:2280px;width:204px;height:206px"><div class="portrait__fill" role="img" aria-label="Portrait photo of a smiling client with glasses"></div></div>
  <div class="sq" style="left:851px;top:2261px;width:59px;height:59px"></div>
  <svg class="abs" style="left:1017px;top:2436px" width="104" height="84"><rect x="68" y="0" width="36" height="56" fill="url(#dots-sm)"/><rect y="56" width="104" height="26" fill="url(#dots-sm)"/></svg>

  <!-- team -->
  <div class="band band--panel" style="top:2560px;height:623px"></div>
  <h2 class="abs serif section-title" style="top:2581px">Our Team</h2>
  <div class="abs section-rule" style="top:2619px"></div>
  <p class="abs section-sub" style="top:2647px">Meet with our team.</p>

  <svg class="abs" style="left:222px;top:2902px" width="104" height="74"><rect x="82" y="0" width="22" height="60" fill="url(#dots-sm)"/><rect y="60" width="104" height="14" fill="url(#dots-sm)"/></svg>
  <svg class="abs" style="left:488px;top:2902px" width="104" height="74"><rect x="82" y="0" width="22" height="60" fill="url(#dots-sm)"/><rect y="60" width="104" height="14" fill="url(#dots-sm)"/></svg>
  <svg class="abs" style="left:754px;top:2902px" width="104" height="74"><rect x="82" y="0" width="22" height="60" fill="url(#dots-sm)"/><rect y="60" width="104" height="14" fill="url(#dots-sm)"/></svg>
  <svg class="abs" style="left:1020px;top:2902px" width="104" height="74"><rect x="82" y="0" width="22" height="60" fill="url(#dots-sm)"/><rect y="60" width="104" height="14" fill="url(#dots-sm)"/></svg>

  <div class="member" style="left:104px;top:2712px"><div class="member__photo" role="img" aria-label="Portrait photo of Chris" style="background:radial-gradient(ellipse at 50% 45%,#6b4a3a 0%,#1a1412 55%,#050505 100%)"></div></div>
  <div class="member" style="left:370px;top:2712px"><div class="member__photo" role="img" aria-label="Portrait photo of Alexa" style="background:radial-gradient(ellipse at 50% 45%,#d8a98c 0%,#a2755c 50%,#6e5140 100%)"></div></div>
  <div class="member" style="left:636px;top:2712px"><div class="member__photo" role="img" aria-label="Portrait photo of Manuella" style="background:radial-gradient(ellipse at 50% 45%,#b58e86 0%,#5560c0 55%,#2d2f7a 100%)"></div></div>
  <div class="member" style="left:902px;top:2712px"><div class="member__photo" role="img" aria-label="Portrait photo of Raul" style="background:radial-gradient(ellipse at 50% 45%,#8a6a55 0%,#3a2f2a 55%,#1d1a19 100%)"></div></div>

  <div class="member__name" style="left:104px">Chris</div><div class="member__role" style="left:104px">Product Designer</div>
  <div class="member__name" style="left:370px">Alexa</div><div class="member__role" style="left:370px">Accountant</div>
  <div class="member__name" style="left:636px">Manuella</div><div class="member__role" style="left:636px">Business and Marketing</div>
  <div class="member__name" style="left:902px">Raul</div><div class="member__role" style="left:902px">Graphic Designer</div>

  <div class="btn team__btn">View all team</div>

  <!-- contact -->
  <h2 class="abs serif section-title" style="top:3240px">Contact Us</h2>
  <div class="abs section-rule" style="top:3278px"></div>
  <p class="abs section-sub" style="top:3305px">Geet a free audit and consultation.</p>

  <p class="abs pitch">It’s easy to get started,<br>We’re just asking for a<br><em>phone call</em> or <em>email</em>.</p>
  <div class="abs contact-label" style="left:104px;top:3589px">Call us at :</div>
  <div class="abs contact-line" style="left:104px;top:3619px">
    <svg width="30" height="30" viewBox="0 0 30 30" fill="none" stroke="#e8b540" stroke-width="2.4"><path d="M7 3 L12 9 L9 13 C11 17 13 19 17 21 L21 18 L27 23 L24 27 C14 27 3 16 3 6 Z"/><path d="M18 4 A8 8 0 0 1 26 12"/><path d="M18 9 A3 3 0 0 1 21 12"/></svg>
    <span>555-014-2276</span>
  </div>
  <div class="abs contact-label" style="left:104px;top:3663px">or email us</div>
  <div class="abs contact-line" style="left:104px;top:3696px">
    <svg width="30" height="28" viewBox="0 0 30 28" fill="none" stroke="#e8b540" stroke-width="2.4"><rect x="2" y="6" width="24" height="18"/><path d="M2 6 L14 16 L26 6"/><path d="M20 24 L28 16"/></svg>
    <span>eliasvarden@mailbox.example</span>
  </div>

  <div class="field" style="top:3385px">Name</div>
  <div class="field" style="top:3448px">Email address</div>
  <div class="field" style="top:3512px">Subject</div>
  <div class="field" style="top:3575px;height:127px">Message</div>
  <div class="btn send">SEND <svg width="16" height="16" viewBox="0 0 16 16" fill="#fff"><path d="M1 7 L15 1 L9 15 L7 9 Z"/></svg></div>

  <!-- footer -->
  <footer class="abs footer">
    <div class="footer__text">COPYRIGHT 2021 &nbsp;&nbsp;| &nbsp;&nbsp;ELIAS VARDEN</div>
    <div class="social" style="left:981px" role="img" aria-label="Social profile link"></div>
    <div class="social" style="left:1028px" role="img" aria-label="Social profile link"></div>
    <div class="social" style="left:1076px" role="img" aria-label="Social profile link"></div>
  </footer>
</div>
</body>
</html>
```